Velnimo.org
Brackwater Residents association
plz star rating....
in the back of the card it should have the following
K&T BULKWARE SUPPLIERS
847 HAZELMOOR ROAD
OLVERTON MA. 02946
we will like the back ground of the card to be red... our colors are red yellow and blue.

```html
<!DOCTYPE html>
<html lang="en">
<head>
<meta charset="utf-8">
<title>Velnimo.org business card</title>
<link href="https://fonts.googleapis.com/css2?family=Source+Sans+3:wght@400;600;700&display=swap" rel="stylesheet">
<style>
  :root {
    --bg: #b3302a;
    --card: #ffffff;
    --brand-blue: #2a9fd8;
    --brand-blue-light: #8fd0f0;
    --brand-yellow: #f2c12e;
    --band-cap: #8a8c8f;
    --ink: #555a60;
    --ink-soft: #7a7f85;
  }
  * { box-sizing: border-box; margin: 0; padding: 0; }
  html, body { width: 1200px; height: 530px; overflow: hidden; }
  body {
    background: var(--bg);
    font-family: "Source Sans 3", Arial, sans-serif;
    position: relative;
  }
  .card {
    position: absolute;
    top: 101px;
    width: 532px;
    height: 390px;
    background: var(--card);
    box-shadow: 0 2px 8px rgba(0,0,0,0.3);
  }
  .card--front { left: 36px; }
  .card--back { left: 612px; }

  .brand {
    position: absolute;
    left: 0; right: 0;
    display: flex;
    justify-content: center;
    align-items: center;
    gap: 12px;
    line-height: 1;
  }
  .brand__mark {
    width: 24px; height: 24px;
    background: var(--brand-yellow);
  }
  .brand__name {
    font-weight: 700;
    font-size: 46px;
    color: var(--brand-blue);
    letter-spacing: 0.5px;
  }
  .card--front .brand { top: 66px; }
  .card--back .brand { top: 62px; }

  .tagline {
    position: absolute;
    top: 124px; left: 0; right: 0;
    text-align: center;
    font-size: 16px;
    font-weight: 600;
    color: var(--brand-blue);
  }

  .band {
    position: absolute;
    left: 0; right: 0;
    top: 180px;
    height: 22px;
    display: flex;
  }
  .band__bar {
    flex: 1;
    background: linear-gradient(to right, var(--brand-blue-light), var(--brand-blue) 55%);
    color: #fff;
    display: flex;
    align-items: center;
    justify-content: center;
  }
  .band__cap { width: 22px; background: var(--band-cap); }

  .person__name { font-size: 15px; font-weight: 600; }
  .person__role { font-size: 11px; margin-left: 8px; }
  .slogan { font-size: 14px; letter-spacing: 4px; }

  .contact {
    position: absolute;
    left: 84px;
    top: 244px;
    font-size: 11.5px;
    color: var(--ink);
    line-height: 20px;
  }
  .contact__row span { margin-right: 12px; }

  .supplier {
    position: absolute;
    left: 0; right: 0;
    top: 216px;
    text-align: center;
    font-size: 11.5px;
    line-height: 17px;
    color: var(--ink);
    letter-spacing: 0.5px;
  }
  .supplier__name { font-weight: 600; }

  .website {
    position: absolute;
    left: 0; right: 0;
    text-align: center;
    font-size: 13px;
    letter-spacing: 1.5px;
    color: var(--ink-soft);
  }
  .website b { color: var(--brand-blue); font-weight: 600; }
  .card--front .website { top: 288px; }
  .card--back .website { top: 278px; }
</style>
</head>
<body>

<section class="card card--front">
  <div class="brand">
    <span class="brand__mark"></span>
    <span class="brand__name">Velnimo.org</span>
  </div>
  <p class="tagline">Brackwater Residents Association</p>
  <div class="band">
    <div class="band__bar">
      <span class="person__name">Daverin Holcomb</span>
      <span class="person__role">President</span>
    </div>
    <div class="band__cap"></div>
  </div>
  <div class="contact">
    <p>58 Fernwick Street, Olverton, Ma 02946</p>
    <p class="contact__row"><span>P: 555-213-0471</span><span>F: 555-214-0382</span><span>E: velnimo2006@mailbox.net</span></p>
  </div>
  <p class="website">www.<b>velnimo</b>.org</p>
</section>

<section class="card card--back">
  <div class="brand">
    <span class="brand__mark"></span>
    <span class="brand__name">Velnimo.org</span>
  </div>
  <div class="band">
    <div class="band__bar"><span class="slogan">WE BUY PROPERTIES</span></div>
    <div class="band__cap"></div>
  </div>
  <div class="supplier">
    <p class="supplier__name">K&amp;T BULKWARE SUPPLIERS</p>
    <p>847 HAZELMOOR ROAD</p>
    <p>OLVERTON MA. 02946</p>
  </div>
  <p class="website">www.<b>velnimo</b>.org</p>
</section>

</body>
</html>
```